Power Point Presentation to Large Audience

Make a consistent look and feel but also make it a compelling presentation. I have attached a summary of my presentation

Target Market(s)

I am making a presentation to investors. Need a consistent look feel but I need it to be simple in design

Requirements
Must have
• Use http://brightlane4jobs.example/ for any background into the company
Nice to have
• My presentation has to be short, less than 10 to 15 minutes. The format I have attached is my basic content, I need it cleaned up and put in a compelling format

```html
<!DOCTYPE html>
<html lang="en">
<head>
<meta charset="utf-8">
<title>BrightLane 4 Jobs — Investor Deck</title>
<link rel="stylesheet" href="https://fonts.googleapis.com/css2?family=Open+Sans:wght@300;400;600;700&family=Saira+Semi+Condensed:wght@300;400&display=swap">
<style>
:root{
  --orange:#f08a1c;
  --orange-deep:#e07a12;
  --orange-soft:#f5a94a;
  --ink:#555a60;
  --grey-dark:#4b4b4d;
  --navy:#3b4759;
  --footer:#58595b;
  --canvas:#f1f1f1;
  --line-g4:#1d5c9a;
  --line-g8:#26a8d2;
  --white:#ffffff;
}
*{box-sizing:border-box;margin:0;padding:0}
html,body{width:1059px;height:1200px;overflow:hidden;background:var(--canvas)}
body{position:relative;font-family:"Open Sans",Arial,sans-serif;color:var(--ink)}
.slide{position:absolute;width:515px;height:290px;background:var(--white);overflow:hidden}
.col-left{left:7px}.col-right{left:537px}
.row-1{top:5px}.row-2{top:305px}.row-3{top:604px}.row-4{top:904px}

.photo{position:absolute;inset:0;background:linear-gradient(180deg,#f3a13a 0%,#f08a1c 55%,#e8831a 100%)}
.photo--road{top:68px;background:linear-gradient(180deg,#f2a64a 0%,#ef9330 45%,#e07d1a 100%)}
.photo--school{background:linear-gradient(180deg,#f4ab55 0%,#ef9a3c 50%,#e98c2a 100%)}

.brand{position:absolute;left:38px;top:24px;display:flex;align-items:center;gap:6px;font-weight:700;font-size:11px;color:var(--orange);letter-spacing:.3px}
.brand-dot{width:14px;height:14px;border-radius:50%;background:var(--orange)}

.quote-mark{position:absolute;left:32px;top:98px;font-family:"Open Sans",sans-serif;font-weight:700;font-size:54px;line-height:1;color:var(--white)}
.quote-text{position:absolute;left:40px;top:148px;width:310px;font-family:"Saira Semi Condensed",sans-serif;font-weight:300;font-size:15px;line-height:18.5px;color:var(--white)}
.quote-rule{position:absolute;left:40px;top:215px;width:180px;height:1px;background:rgba(255,255,255,.7)}
.quote-author{position:absolute;left:230px;top:204px;font-family:"Saira Semi Condensed",sans-serif;font-size:15px;color:var(--white)}

.hero-icon{position:absolute;left:240px;top:82px}
.hero-title{position:absolute;left:0;right:0;top:124px;text-align:center;font-family:"Saira Semi Condensed",sans-serif;font-size:29px;line-height:34px;color:var(--white)}

.slide-title{position:absolute;left:40px;top:16px;font-weight:300;font-size:19px;color:var(--orange)}
.title-rule{position:absolute;left:36px;top:47px;width:234px;height:1px;background:#555}

.footer{position:absolute;left:0;right:0;bottom:0;height:15px;background:var(--footer);font-size:5px;color:#ddd;padding-left:4px;line-height:15px}
.footer-brand{position:absolute;right:24px;top:0;height:15px;padding:0 4px;background:var(--white);font-size:8px;font-weight:600;color:#666;line-height:15px}
.page-num{position:absolute;right:3px;top:0;width:17px;height:15px;background:var(--orange);color:var(--white);font-size:5px;text-align:center;line-height:15px}

.model-left{position:absolute;right:350px;top:97px;width:130px;text-align:right;font-size:6.2px;line-height:9px;color:#8a8a8a;font-weight:300}
.model-left strong{display:block;font-weight:600;color:#444;font-size:7px;margin-bottom:2px}
.model-right{position:absolute;left:353px;top:102px;width:140px;font-size:6.4px;line-height:10px;color:#9a9a9a;font-style:italic;font-weight:300}
.model-right strong{display:block;font-style:normal;font-weight:400;color:var(--orange);margin-bottom:1px}
.model-right u{font-weight:600;color:#6a6a6a}

.point-text{position:absolute;font-size:8.6px;line-height:12.3px;color:#707070;font-weight:300}
.point-text--center{text-align:center}
.icon-disc{position:absolute;width:56px;height:56px;border-radius:50%}

.chart-card{position:absolute;left:108px;top:51px;width:383px;height:210px;background:var(--white);border-radius:14px;box-shadow:0 0 8px rgba(0,0,0,.18)}
.chart-card svg{display:block}

.stat{position:absolute;left:0;right:0;top:92px;text-align:center;font-family:"Saira Semi Condensed",sans-serif;font-size:21px;line-height:27px;color:var(--white)}
.stat-number{font-size:58px;vertical-align:-6px;padding:0 10px}
.source{position:absolute;left:25px;bottom:28px;font-size:5px;color:rgba(255,255,255,.85)}
</style>
</head>
<body>

<!-- Slide 1: opening quote -->
<section class="slide col-left row-1">
  <div class="brand"><span class="brand-dot"></span>BRIGHTLANE 4 JOBS</div>
  <div class="photo photo--road" role="img" aria-label="Open desert road stretching to the horizon, orange toned"></div>
  <div class="quote-mark">&#8221;</div>
  <p class="quote-text">To find out what one is fitted to do, and to secure an opportunity to do it, is the key to happiness.</p>
  <div class="quote-rule"></div>
  <div class="quote-author">Harlan Voss</div>
</section>

<!-- Slide 2: question -->
<section class="slide col-right row-1">
  <div class="photo" role="img" aria-label="Hazy orange sky over hills"></div>
  <svg class="hero-icon" width="34" height="30" viewBox="0 0 34 30" fill="none" stroke="#fff" stroke-width="1.6">
    <path d="M3 9 L17 3 L31 9 L17 15 Z"/>
    <path d="M9 12 V20 C13 23 21 23 25 20 V12"/>
    <path d="M29 10 V17"/>
  </svg>
  <h1 class="hero-title">Has personalized learning has<br>gotten it wrong?</h1>
</section>

<!-- Slide 3: model -->
<section class="slide col-left row-2">
  <h2 class="slide-title">Personalized Learning Model</h2>
  <div class="title-rule"></div>
  <div class="model-left"><strong>Personalized Learning Results:</strong>"The evidence base is very weak at this point," said Martin R. Hale, a senior scientist and the group's distinguished chair in education innovation.</div>
  <svg style="position:absolute;left:170px;top:85px" width="180" height="160" viewBox="0 0 180 160">
    <path d="M34 33 C70 20 110 20 140 33" stroke="#f08a1c" stroke-width="30" fill="none"/>
    <path d="M34 33 C20 70 20 100 33 124" stroke="#4b4b4d" stroke-width="22" fill="none"/>
    <circle cx="34" cy="33" r="31" fill="#4b4b4d"/>
    <circle cx="34" cy="33" r="24" fill="#fff"/>
    <circle cx="140" cy="33" r="33" fill="#f08a1c"/>
    <circle cx="140" cy="33" r="25" fill="#fff"/>
    <circle cx="33" cy="124" r="30" fill="#f08a1c"/>
    <circle cx="33" cy="124" r="23" fill="#fff"/>
    <rect x="25" y="22" width="16" height="20" rx="1.5" stroke="#4b4b4d" stroke-width="1.4" fill="none"/>
    <circle cx="35" cy="34" r="5" stroke="#4b4b4d" stroke-width="1.4" fill="none"/>
    <circle cx="137" cy="30" r="7" stroke="#f08a1c" stroke-width="2" fill="none"/>
    <path d="M142 35 L149 42" stroke="#f08a1c" stroke-width="2.4"/>
    <circle cx="33" cy="119" r="5" stroke="#4b4b4d" stroke-width="1.3" fill="#f5d84a"/>
    <path d="M31 125 H35 M31 128 H35" stroke="#4b4b4d" stroke-width="1.2"/>
  </svg>
  <div class="model-right"><strong>Personalized Learning Model Definition:</strong>Personalized-learning models seek to adapt the pace of learning and the instructional strategies being used to best fit each individual child's strengths, weaknesses, and <u>interests.</u></div>
  <footer class="footer">NX7learn&#8482; BrightLane4Jobs&#8482; 2018 Trademark NX7learn, LLC<span class="footer-brand">NX7learn</span><span class="page-num">3</span></footer>
</section>

<!-- Slide 4: where wrong (a) -->
<section class="slide col-right row-2">
  <h2 class="slide-title">Where has it Gone Wrong?</h2>
  <div class="title-rule"></div>
  <svg style="position:absolute;left:38px;top:117px" width="58" height="58"><circle cx="29" cy="29" r="29" fill="#3b4759"/><rect x="14" y="14" width="30" height="30" rx="2" fill="#f4f4f4"/></svg>
  <p class="point-text" style="left:108px;top:100px;width:140px">many versions of personalized learning seek to change or replace fundamental processes that shape the day-to-day life of schools—everything from how teachers prepare lessons to how students are graded.</p>
  <svg style="position:absolute;left:262px;top:117px" width="58" height="58"><circle cx="29" cy="29" r="29" fill="#3b4759"/><rect x="14" y="14" width="30" height="30" rx="2" fill="#f4f4f4"/></svg>
  <p class="point-text" style="left:332px;top:112px;width:135px">HINT:&nbsp; We weren't doing that well to begin with, replicating what doesn't work into personalized learning plans doesn't change behavior</p>
  <footer class="footer">NX7learn&#8482; BrightLane4Jobs&#8482; 2018 Trademark NX7learn, LLC<span class="footer-brand">NX7learn</span><span class="page-num">4</span></footer>
</section>

<!-- Slide 5: where wrong (b) -->
<section class="slide col-left row-3">
  <h2 class="slide-title">Where has it Gone Wrong?</h2>
  <div class="title-rule"></div>
  <svg class="icon-disc" style="left:116px;top:80px" viewBox="0 0 56 56">
    <circle cx="28" cy="28" r="28" fill="#f08a1c"/>
    <g stroke="#fff" stroke-width="1.4" fill="none"><circle cx="28" cy="22" r="6"/><path d="M25 28 V33 H31 V28"/><path d="M17 42 C17 35 22 33 28 33 C34 33 39 35 39 42"/><path d="M24 36 V42 M32 36 V42"/></g>
  </svg>
  <p class="point-text point-text--center" style="left:92px;top:150px;width:130px">Many versions of personalized learning seek to change or replace fundamental processes that shape the day-to-day life of schools—everything from how teachers prepare lessons to how students are graded.</p>
  <svg class="icon-disc" style="left:335px;top:80px" viewBox="0 0 56 56">
    <circle cx="28" cy="28" r="28" fill="#f08a1c"/>
    <g stroke="#fff" stroke-width="1.3" fill="none"><circle cx="20" cy="20" r="3"/><circle cx="28" cy="20" r="3"/><circle cx="36" cy="20" r="3"/><path d="M15 32 C15 27 25 27 25 32 M23 32 C23 27 33 27 33 32 M31 32 C31 27 41 27 41 32"/><path d="M20 35 V41 M28 35 V43 M34 38 H41 M34 41 H41"/></g>
  </svg>
  <p class="point-text point-text--center" style="left:306px;top:150px;width:120px">HINT:&nbsp; We weren't doing that well to begin with, replicating what doesn't work into personalized learning plans doesn't change behavior</p>
  <footer class="footer">NX7learn&#8482; BrightLane4Jobs&#8482; 2018 Trademark NX7learn, LLC<span class="footer-brand">NX7learn</span><span class="page-num">5</span></footer>
</section>

<!-- Slide 6: math chart -->
<section class="slide col-right row-3">
  <h2 class="slide-title">NSAE Math Scores</h2>
  <div class="title-rule"></div>
  <div class="chart-card">
    <svg width="383" height="210" viewBox="0 0 383 210" font-family="Open Sans, sans-serif">
      <text x="191" y="15" text-anchor="middle" font-size="5.5" font-weight="700" fill="#1d4f8a">Figure 1: NSAE math score trends for grades 4 and 8</text>
      <g stroke="#bbb" stroke-width=".5"><line x1="66" y1="30" x2="350" y2="30"/><line x1="66" y1="58.75" x2="350" y2="58.75"/><line x1="66" y1="87.5" x2="350" y2="87.5"/><line x1="66" y1="116.25" x2="350" y2="116.25"/><line x1="66" y1="145" x2="350" y2="145" stroke="#555"/></g>
      <g font-size="4.5" fill="#444" text-anchor="end"><text x="62" y="32">0.8</text><text x="62" y="60.5">0.6</text><text x="62" y="89">0.4</text><text x="62" y="118">0.2</text><text x="62" y="147">0.0</text></g>
      <text transform="translate(34 88) rotate(-90)" text-anchor="middle" font-size="4.2" font-weight="700" fill="#1d4f8a">Difference from 1996 score<tspan x="0" dy="5">(in 1996 standard deviations)</tspan></text>
      <g font-size="4.2" fill="#444" text-anchor="end">
        <text transform="translate(74 150) rotate(-90)">1996</text><text transform="translate(104 150) rotate(-90)">2000</text><text transform="translate(135 150) rotate(-90)">2003</text><text transform="translate(165 150) rotate(-90)">2005</text><text transform="translate(195 150) rotate(-90)">2007</text><text transform="translate(226 150) rotate(-90)">2009</text><text transform="translate(256 150) rotate(-90)">2011</text><text transform="translate(286 150) rotate(-90)">2013</text><text transform="translate(316 150) rotate(-90)">2015</text><text transform="translate(347 150) rotate(-90)">2017</text>
      </g>
      <text x="191" y="172" text-anchor="middle" font-size="4.5" font-weight="700" fill="#1d4f8a">Year</text>
      <polyline fill="none" stroke="#1d5c9a" stroke-width="1.2" points="72,145 102,133.5 133,93.3 163,80.3 193,70.3 224,70.3 254,65.9 284,61.6 314,70.3 345,70.3"/>
      <polyline fill="none" stroke="#26a8d2" stroke-width="1.2" points="72,145 102,136.4 133,114.8 163,110.5 193,103.3 224,94.7 254,91.8 284,87.5 314,99 345,94.7"/>
      <g fill="#1d5c9a"><circle cx="72" cy="145" r="1.3"/><circle cx="102" cy="133.5" r="1.3"/><circle cx="133" cy="93.3" r="1.3"/><circle cx="163" cy="80.3" r="1.3"/><circle cx="193" cy="70.3" r="1.3"/><circle cx="224" cy="70.3" r="1.3"/><circle cx="254" cy="65.9" r="1.3"/><circle cx="284" cy="61.6" r="1.3"/><circle cx="314" cy="70.3" r="1.3"/><circle cx="345" cy="70.3" r="1.3"/></g>
      <g fill="#26a8d2"><circle cx="102" cy="136.4" r="1.3"/><circle cx="133" cy="114.8" r="1.3"/><circle cx="163" cy="110.5" r="1.3"/><circle cx="193" cy="103.3" r="1.3"/><circle cx="224" cy="94.7" r="1.3"/><circle cx="254" cy="91.8" r="1.3"/><circle cx="284" cy="87.5" r="1.3"/><circle cx="314" cy="99" r="1.3"/><circle cx="345" cy="94.7" r="1.3"/></g>
      <g font-size="4.3" fill="#333" text-anchor="middle">
        <text x="72" y="140">0.00</text><text x="90" y="129">0.06</text><text x="113" y="127">0.08</text><text x="133" y="89">0.36</text><text x="163" y="76">0.45</text><text x="193" y="66">0.52</text><text x="224" y="66">0.52</text><text x="254" y="61.5">0.55</text><text x="284" y="57">0.58</text><text x="314" y="66">0.52</text><text x="345" y="66">0.52</text>
        <text x="133" y="111">0.21</text><text x="163" y="106">0.24</text><text x="193" y="99">0.29</text><text x="224" y="90">0.35</text><text x="254" y="87.5">0.37</text><text x="284" y="83">0.40</text><text x="314" y="107">0.32</text><text x="345" y="90">0.35</text>
      </g>
      <g font-size="4.2" fill="#444"><line x1="136" y1="181" x2="148" y2="181" stroke="#1d5c9a"/><circle cx="142" cy="181" r="1.2" fill="#1d5c9a"/><text x="151" y="182.5">Grade 4</text><line x1="216" y1="181" x2="228" y2="181" stroke="#26a8d2"/><circle cx="222" cy="181" r="1.2" fill="#26a8d2"/><text x="231" y="182.5">Grade 8</text></g>
      <text x="18" y="196" font-size="4" font-style="italic" fill="#333">Source: Authors' calculations based on NSAE Data Explorer.</text>
      <text x="370" y="198" text-anchor="end" font-size="10" fill="#1d4f8a">RIDGEFIELD</text>
    </svg>
  </div>
  <footer class="footer">NX7learn&#8482; BrightLane4Jobs&#8482; 2018 Trademark NX7learn, LLC<span class="footer-brand">NX7learn</span><span class="page-num">6</span></footer>
</section>

<!-- Slide 7: reading chart -->
<section class="slide col-left row-4">
  <h2 class="slide-title">NSAE Reading</h2>
  <div class="title-rule"></div>
  <div class="chart-card">
    <svg width="383" height="210" viewBox="0 0 383 210" font-family="Open Sans, sans-serif">
      <text x="191" y="15" text-anchor="middle" font-size="5.5" font-weight="700" fill="#1d4f8a">Figure 2: NSAE reading score trends for grades 4 and 8</text>
      <g stroke="#bbb" stroke-width=".5"><line x1="66" y1="30" x2="350" y2="30"/><line x1="66" y1="62.5" x2="350" y2="62.5"/><line x1="66" y1="95" x2="350" y2="95" stroke="#555"/><line x1="66" y1="127.5" x2="350" y2="127.5"/><line x1="66" y1="160" x2="350" y2="160"/></g>
      <g font-size="4.5" fill="#444" text-anchor="end"><text x="62" y="32">0.4</text><text x="62" y="64.5">0.2</text><text x="62" y="97">0.0</text><text x="62" y="129.5">-0.2</text><text x="62" y="162">-0.4</text></g>
      <text transform="translate(34 95) rotate(-90)" text-anchor="middle" font-size="4.2" font-weight="700" fill="#1d4f8a">Difference from 1998 score<tspan x="0" dy="5">(in 1998 standard deviations)</tspan></text>
      <g font-size="4.2" fill="#444" text-anchor="end">
        <text transform="translate(74 165) rotate(-90)">1998</text><text transform="translate(101 165) rotate(-90)">2000</text><text transform="translate(128 165) rotate(-90)">2002</text><text transform="translate(156 165) rotate(-90)">2003</text><text transform="translate(183 165) rotate(-90)">2005</text><text transform="translate(210 165) rotate(-90)">2007</text><text transform="translate(238 165) rotate(-90)">2009</text><text transform="translate(265 165) rotate(-90)">2011</text><text transform="translate(292 165) rotate(-90)">2013</text><text transform="translate(319 165) rotate(-90)">2015</text><text transform="translate(347 165) rotate(-90)">2017</text>
      </g>
      <text x="191" y="185" text-anchor="middle" font-size="4.5" font-weight="700" fill="#1d4f8a">Year</text>
      <polyline fill="none" stroke="#1d5c9a" stroke-width="1.2" points="72,95 99.3,103.1 126.6,78.75 153.9,82 181.2,78.75 208.5,70.6 235.8,70.6 263.1,70.6 290.4,65.75 317.7,60.9 345,65.75"/>
      <polyline fill="none" stroke="#26a8d2" stroke-width="1.2" points="72,95 126.6,90.1 153.9,95 181.2,99.9 208.5,95 235.8,90.1 263.1,85.25 290.4,72.25 317.7,85.25 345,77.1"/>
      <g font-size="4.3" fill="#333" text-anchor="middle">
        <text x="72" y="102">0.00</text><text x="101" y="111">-0.05</text><text x="119" y="74">0.10</text><text x="156" y="78">0.08</text><text x="181" y="74">0.10</text><text x="208" y="66">0.15</text><text x="236" y="66">0.15</text><text x="263" y="66">0.15</text><text x="290" y="61">0.18</text><text x="318" y="56">0.21</text><text x="345" y="61">0.18</text>
        <text x="123" y="86">0.03</text><text x="154" y="102">0.00</text><text x="181" y="107">-0.03</text><text x="208" y="102">0.00</text><text x="236" y="97">0.03</text><text x="263" y="81">0.06</text><text x="290" y="80">0.14</text><text x="318" y="92">0.06</text><text x="345" y="85">0.11</text>
      </g>
      <g font-size="4.2" fill="#444"><line x1="136" y1="194" x2="148" y2="194" stroke="#1d5c9a"/><circle cx="142" cy="194" r="1.2" fill="#1d5c9a"/><text x="151" y="195.5">Grade 4</text><line x1="226" y1="194" x2="238" y2="194" stroke="#26a8d2"/><circle cx="232" cy="194" r="1.2" fill="#26a8d2"/><text x="241" y="195.5">Grade 8</text></g>
      <text x="22" y="203" font-size="4" font-style="italic" fill="#333">Source: Authors' calculations based on NSAE Data Explorer.</text>
      <text x="364" y="202" text-anchor="end" font-size="10" fill="#1d4f8a">RIDGEFIELD</text>
    </svg>
  </div>
  <footer class="footer">NX7learn&#8482; BrightLane4Jobs&#8482; 2018 Trademark NX7learn, LLC<span class="footer-brand">NX7learn</span><span class="page-num">7</span></footer>
</section>

<!-- Slide 8: statistic -->
<section class="slide col-right row-4">
  <div class="photo photo--school" role="img" aria-label="High school building and schoolyard, orange toned"></div>
  <p class="stat">Nationwide, there are<span class="stat-number">2,397</span>high<br>schools, , that do not graduate one-third or more of<br>their students.</p>
  <p class="source">Source: http://www.gradtracker.example/report_2016_full.pdf (accessed August 25, 2016)</p>
</section>

</body>
</html>
```